We are looking for a graphic that visually demonstrates the interconnectivy of various different web applications. We work with iPaaS platforms like Tivrel.com where we enable workflows across all the various web applications. We would like to graphically show this for a page on our website.

Businesses use a host of different web apps such as DealBrook, LedgerPine, Zorvik, Halvenco, Brisk Mailer, Chatterloop, WorkWeave, and so on. We want to be able to show that Web apps can be connected for various tools such as CRM, Document Management, Markeing, ERP/Accounting, Sales, Legal and more to help drive productivity and efficiency by passing data and/or documents across these applications automatically.

```html
<!DOCTYPE html>
<html lang="en">
<head>
<meta charset="utf-8">
<title>Interconnectivity Of Various Different Web Applications</title>
<link href="https://fonts.googleapis.com/css2?family=Montserrat:wght@400;500&display=swap" rel="stylesheet">
<style>
  :root {
    --light-bg: #f0f1f2;
    --light-ink: #1c1c1c;
    --light-title: #4a4a4a;
    --light-ring: #dcdde0;
    --dark-ink: #ffffff;
    --dark-ring: #4a4a4a;
    --hub-blue: #29a9e1;
    --cms-purple: #93278f;
    --planner-pink: #ed1e79;
    --planner-arc: #f15a5a;
    --messaging-yellow: #ffd54f;
    --messaging-arc: #fde8a8;
    --storage-green: #5ad894;
    --storage-arc: #22c47a;
  }
  html, body {
    margin: 0;
    padding: 0;
    width: 800px;
    height: 1200px;
    overflow: hidden;
    background: #000;
  }
  .artboard {
    display: block;
    width: 800px;
    height: 1200px;
    font-family: "Montserrat", sans-serif;
  }
  .theme-light { color: var(--light-ink); --ring: var(--light-ring); }
  .theme-dark { color: var(--dark-ink); --ring: var(--dark-ring); }
  .section-title { font-size: 30px; font-weight: 400; text-anchor: middle; letter-spacing: 0.3px; }
  .theme-light .section-title { fill: var(--light-title); }
  .theme-dark .section-title { fill: var(--dark-ink); }
  .app-label { font-size: 30px; font-weight: 400; fill: currentColor; letter-spacing: 0.3px; }
  .link-line { stroke: currentColor; stroke-width: 2; stroke-dasharray: 9 6; fill: none; }
  .guide-ring { fill: none; stroke: var(--ring); stroke-width: 1.2; stroke-dasharray: 3 3; }
  .accent-arc { fill: none; stroke-width: 2.2; }
  .hub-arc { fill: none; stroke: var(--hub-blue); stroke-width: 4; }
</style>
</head>
<body>
<svg class="artboard" viewBox="0 0 1568 2353" xmlns="http://www.w3.org/2000/svg" role="img" aria-label="Web applications connected through a central routing hub, shown in light and dark themes">
  <defs>
    <radialGradient id="dark-glow" cx="777" cy="1788" r="950" gradientUnits="userSpaceOnUse">
      <stop offset="0" stop-color="#474747"/>
      <stop offset="0.55" stop-color="#1c1c1c"/>
      <stop offset="1" stop-color="#000000"/>
    </radialGradient>

    <g id="node-rings">
      <circle class="guide-ring" r="136"/>
      <circle class="guide-ring" r="124"/>
    </g>

    <g id="connection-diagram">
      <!-- connectors -->
      <line class="link-line" x1="418" y1="448" x2="566" y2="522"/>
      <line class="link-line" x1="1113" y1="438" x2="950" y2="522"/>
      <line class="link-line" x1="418" y1="785" x2="566" y2="714"/>
      <line class="link-line" x1="1105" y1="790" x2="950" y2="714"/>

      <rect class="plug" x="564" y="518" width="24" height="24" transform="rotate(27 576 530)" fill="var(--cms-purple)"/>
      <rect class="plug" x="928" y="518" width="24" height="24" transform="rotate(-27 940 530)" fill="var(--planner-pink)"/>
      <rect class="plug" x="564" y="697" width="24" height="24" transform="rotate(-27 576 709)" fill="var(--messaging-yellow)"/>
      <rect class="plug" x="928" y="696" width="24" height="24" transform="rotate(27 940 708)" fill="var(--storage-arc)"/>

      <!-- hub -->
      <g class="hub-node" transform="translate(760 621)">
        <circle class="guide-ring" r="176"/>
        <circle class="guide-ring" r="160"/>
        <circle class="hub-arc" r="176" stroke-dasharray="255 851" transform="rotate(170)"/>
        <circle class="hub-arc" r="161" stroke-dasharray="244 768" transform="rotate(40)"/>
        <circle class="hub-arc" r="148" stroke-dasharray="232 698" transform="rotate(-90)"/>
        <circle r="102" fill="var(--hub-blue)" role="img" aria-label="Cloud routing hub icon"/>
      </g>
      <text class="app-label" x="673" y="876">Routing/Hub</text>

      <!-- CMS app -->
      <g class="app-node" transform="translate(291 381)">
        <use href="#node-rings"/>
        <circle class="accent-arc" r="136" stroke="var(--cms-purple)" stroke-dasharray="207 102 195 351" transform="rotate(40)"/>
        <circle class="accent-arc" r="113" stroke="var(--cms-purple)" stroke-dasharray="178 532" transform="rotate(-90)"/>
        <circle r="78" fill="var(--cms-purple)" role="img" aria-label="Content management app icon"/>
      </g>
      <text class="app-label" x="181" y="573">CMS APP</text>

      <!-- Planner app -->
      <g class="app-node" transform="translate(1247 377)">
        <use href="#node-rings"/>
        <circle class="accent-arc" r="136" stroke="var(--planner-arc)" stroke-dasharray="207 102 195 351" transform="rotate(40)"/>
        <circle class="accent-arc" r="113" stroke="var(--planner-arc)" stroke-dasharray="178 532" transform="rotate(-90)"/>
        <circle r="78" fill="var(--planner-pink)" role="img" aria-label="Planner app icon"/>
      </g>
      <text class="app-label" x="1140" y="573">Planner APP</text>

      <!-- Messaging app -->
      <g class="app-node" transform="translate(289 853)">
        <use href="#node-rings"/>
        <circle class="accent-arc" r="136" stroke="var(--messaging-arc)" stroke-dasharray="207 102 195 351" transform="rotate(40)"/>
        <circle class="accent-arc" r="113" stroke="var(--messaging-arc)" stroke-dasharray="178 532" transform="rotate(-90)"/>
        <circle r="78" fill="var(--messaging-yellow)" role="img" aria-label="Messaging app icon"/>
      </g>
      <text class="app-label" x="182" y="1031">Messaging APP</text>

      <!-- Storage app -->
      <g class="app-node" transform="translate(1233 853)">
        <use href="#node-rings"/>
        <circle class="accent-arc" r="136" stroke="var(--storage-arc)" stroke-dasharray="207 102 195 351" transform="rotate(40)"/>
        <circle class="accent-arc" r="113" stroke="var(--storage-arc)" stroke-dasharray="178 532" transform="rotate(-90)"/>
        <circle r="78" fill="var(--storage-green)" role="img" aria-label="Storage app icon"/>
      </g>
      <text class="app-label" x="1140" y="1031">Storage APP</text>
    </g>
  </defs>

  <g class="theme-light">
    <rect x="0" y="0" width="1568" height="1214" fill="var(--light-bg)"/>
    <text class="section-title" x="782" y="166">Interconnectivy Of Various Different Web Applications</text>
    <use href="#connection-diagram"/>
  </g>

  <g class="theme-dark">
    <rect x="0" y="1214" width="1568" height="1139" fill="url(#dark-glow)"/>
    <text class="section-title" x="774" y="1315">Interconnectivy Of Various Different Web Applications</text>
    <use href="#connection-diagram" transform="translate(17 1167)"/>
  </g>
</svg>
</body>
</html>
```